Corporate Design für Pfannwerk GmbH
Wir hatten von Anfang an eine hervorragende Zusammenarbeit mit KZ47. Schnelle und klare Kommunikation, sofortige Umsetzung unserer Ideen und Vorstellungen während des Prozesses!! Wir sind mit Allem sehr zufrieden.
Zielgruppe
Pfannwerk ist der einzige Küchenhändler am Starnberger See. Wir sehen uns als Premium Anbieter in unserem Segment mit 30 jähriger Branchenerfahrung. Unser Angebot richtet sich an eine Zielgruppe zwischen 25 und 50 Jahren mit mittlerem bis gehobenem Einkommen. Wir versuchen aber auch 'sozial Schwächere' glücklich zu machen.
Die Besonderheit unseres Unternehmens besteht darin, Küchen als erster Multi- Channel-Anbieter zu verkaufen, d.h.:
- die Kunden können ihre Küche online über unser Planungstool gestalten und erhalten eine Online-Beratung via Skype bzw. FaceTime
- die Kunden können nach Vergabe eines individuellen Beratungstermins zu uns in den Showroom kommen
- wir fahren zum Kunden, um eine exklusive Vor-Ort-Beratung durchzuführen
Letzter Punkt ist der Schwerpunkt unserer Beratungsleistung.
Zum Slogan: Küchenkauf ist oft ein nerviger und vor allem zeitraubender Prozess. Dadurch, dass wir zum Kunden fahren, ihn Online beraten, er ausschließlich exklusive Einzeltermine bekommt, erhält der Kunde uneingeschränkte Zeit durch uns und wir schenken ihm zweifelsohne Zeit, die er für sinnvollere Dinge, wie Familie, Freunde, Hobbies oder sich selbst nutzen kann.
Aufgabenstellung
Unser Geschäftsauftritt soll Exklusivität, Wärme und Persönlichkeit ausstrahlen.
Unsere bevorzugten Farben sind schwarz, rot und/oder weiß. Wir sind aber auch offen für andere kreative Vorschläge. Der Name Pfannwerk ist bereits geschützt. Die Wort-Bildmarke soll ebenfalls geschützt werden.
Als Unternehmer Persönlichkeiten sind wir ein bißchen 'verrückt' und anders als die meisten in diesem Bereich. Dies darf in unserem Geschäftsauftritt durchaus zu sehen sein ohne Seriosität einzubüßen ;-).
Gleichzeitig leben wir Werte, wie Wertschätzung, Klarheit, Respekt, Authentizität, Vertrauen Seriosität, Loyalität, Flexibilität und Individualität.

```html
<!DOCTYPE html>
<html lang="de">
<head>
<meta charset="utf-8">
<title>Pfannwerk GmbH – Visitenkarte</title>
<link rel="stylesheet" href="https://fonts.googleapis.com/css2?family=Montserrat:wght@400;500&display=swap">
<style>
  :root {
    --copper: #c0703d;
    --ink: #1d1d1d;
    --muted: #6b6b6b;
    --rule: #9a9a9a;
    --paper: #ffffff;
    --backdrop: #e6e4e1;
  }
  * { margin: 0; padding: 0; box-sizing: border-box; }
  html, body {
    width: 1200px; height: 842px; overflow: hidden;
    background: var(--backdrop);
    font-family: "Montserrat", sans-serif;
  }
  .sheet {
    width: 1200px; height: 842px;
    display: flex; align-items: center; justify-content: center; gap: 60px;
  }
  .card {
    width: 520px; height: 336px;
    background: var(--paper);
    box-shadow: 0 2px 10px rgba(0,0,0,.12);
    position: relative;
  }
  /* Front: name and tagline */
  .card--front { display: flex; align-items: center; justify-content: center; }
  .brand { text-align: center; }
  .brand__name {
    color: var(--copper); font-weight: 400; font-size: 44px; letter-spacing: 1px; line-height: 1;
  }
  .brand__tagline {
    color: var(--muted); font-weight: 400; font-size: 12px; letter-spacing: 0.5px;
    margin-top: 12px;
  }
  /* Back: contact */
  .card--back { display: flex; align-items: center; padding: 0 40px; }
  .contact {
    display: flex; flex-direction: column; gap: 24px; text-align: right;
  }
  .contact__group {
    padding-right: 16px; border-right: 1px solid var(--rule);
  }
  .person__name { color: var(--copper); font-size: 15px; font-weight: 400; line-height: 1.2; }
  .person__role { color: var(--ink); font-size: 10px; line-height: 1.3; }
  .person__role + .person__name { margin-top: 8px; }
  .contact__details { color: var(--ink); font-size: 10px; line-height: 1.45; }
  .contact__details p + p { margin-top: 9px; }
  .contact__web { font-weight: 500; }
  .card__mark {
    margin-left: auto; color: var(--copper); font-size: 26px; font-weight: 400;
    display: flex; align-items: center; gap: 10px;
  }
  .card__mark-dot { width: 12px; height: 12px; border-radius: 50%; background: var(--copper); }
</style>
</head>
<body>
<main class="sheet">
  <section class="card card--front" aria-label="Vorderseite">
    <div class="brand">
      <div class="brand__name">Pfannwerk</div>
      <div class="brand__tagline">Ihre Küche, Ihr Takt</div>
    </div>
  </section>

  <section class="card card--back" aria-label="Rückseite">
    <div class="contact">
      <div class="contact__group contact__names">
        <div class="person__name">Marlene Weidinger</div>
        <div class="person__role">Geschäftsführerin</div>
        <div class="person__name">Jonas Reitberger</div>
        <div class="person__role">Geschäftsleiter</div>
      </div>
      <div class="contact__group contact__details">
        <p>Pfannwerk GmbH<br>Seestraße 14<br>82319 Starnberg</p>
        <p>Fon: +49 8151 442 31 70<br>Fax: +49 8151 442 31 79</p>
        <p>info@pfannwerk-kuechen.de<br><span class="contact__web">www.pfannwerk-kuechen.de</span></p>
      </div>
    </div>
    <div class="card__mark"><span class="card__mark-dot"></span>Pfannwerk</div>
  </section>
</main>
</body>
</html>
```